Solar appointment reminder card

We are looking for a new design for our appointment reminder card since we have changed our logo. The card should have the new logo along with space for the employee to hand write the customers appointment date, time, the employees name and phone number.
I've uploaded what our old basic appointment card looked like and our new logo.

The cards should be in a standard business card size and could be horizontal or vertical.

```html
<!DOCTYPE html>
<html lang="en">
<head>
<meta charset="utf-8">
<title>Brightvale Solar – Appointment Card</title>
<link href="https://fonts.googleapis.com/css2?family=Montserrat:wght@400;500;700;800&display=swap" rel="stylesheet">
<style>
  :root {
    --sun-yellow: #fbb515;
    --sun-orange: #f39a1e;
    --ink: #111111;
    --text: #1c1c1c;
    --paper: #ffffff;
    --map-grey: #e4e4e4;
    --map-gold: #f3aa10;
    --page: #ffffff;
    --rule: #dcdcdc;
  }
  * { box-sizing: border-box; margin: 0; padding: 0; }
  html, body {
    width: 1200px; height: 1200px; overflow: hidden;
    background: var(--page);
    font-family: "Montserrat", sans-serif;
  }
  .sheet {
    width: 1200px; height: 1200px;
    display: flex; flex-direction: column; align-items: center; justify-content: center;
    gap: 60px;
  }
  .card {
    position: relative;
    width: 880px; height: 503px;
    overflow: hidden;
    box-shadow: 0 4px 14px rgba(0,0,0,0.22);
  }

  /* Front */
  .card--front { background: var(--sun-yellow); }
  .card--front .pattern-band {
    position: absolute; left: 0; top: 0; width: 100%; height: 120px;
    background: linear-gradient(180deg, rgba(17,17,17,0.55) 0%, rgba(17,17,17,0.22) 45%, rgba(17,17,17,0) 100%);
  }
  .card--front .world-map {
    position: absolute; left: 75px; top: 80px; width: 730px; height: 400px;
    background: radial-gradient(ellipse at center, var(--map-gold) 0%, rgba(243,170,16,0.5) 55%, rgba(243,170,16,0) 80%);
    border-radius: 40px;
  }
  .brand {
    position: absolute; display: flex; align-items: center; gap: 18px;
  }
  .brand__mark {
    width: 92px; height: 92px; border-radius: 50%;
  }
  .brand__words { display: flex; flex-direction: column; }
  .brand__name {
    font-weight: 800; font-size: 92px; line-height: 0.9; letter-spacing: -1px;
  }
  .brand__tagline {
    font-weight: 800; font-size: 19px; letter-spacing: 5px; margin-top: 8px;
  }
  .card--front .brand { left: 265px; top: 178px; color: var(--ink); }
  .card--front .brand__mark { background: var(--ink); }
  .web-link {
    position: absolute; left: 0; right: 0; top: 405px;
    display: flex; justify-content: center; align-items: center; gap: 12px;
    font-weight: 700; font-size: 19px; color: var(--ink);
  }

  /* Back */
  .card--back { background: var(--paper); }
  .card--back .pattern-band {
    position: absolute; left: 0; top: 0; width: 100%; height: 110px;
    background: linear-gradient(180deg, rgba(251,181,21,0.55) 0%, rgba(251,181,21,0.2) 55%, rgba(251,181,21,0) 100%);
  }
  .card--back .world-map {
    position: absolute; left: 30px; top: 70px; width: 330px; height: 400px;
    background: radial-gradient(ellipse at 50% 45%, var(--map-grey) 0%, rgba(228,228,228,0.6) 55%, rgba(228,228,228,0) 80%);
    border-radius: 40px;
  }
  .card--back .brand { left: 30px; top: 205px; color: var(--sun-orange); gap: 12px; }
  .card--back .brand__mark { width: 56px; height: 56px; background: var(--sun-yellow); }
  .card--back .brand__name { font-size: 60px; }
  .card--back .brand__tagline { font-size: 13px; letter-spacing: 3px; margin-top: 6px; }
  .form-title {
    position: absolute; left: 485px; top: 42px;
    font-weight: 500; font-size: 36px; color: var(--ink);
  }
  .form-panel {
    position: absolute; left: 353px; top: 92px; right: 0; bottom: 0;
    background: var(--paper);
    border-left: 2px solid var(--rule);
  }
  .form-field {
    position: absolute; left: 18px;
    font-weight: 500; font-size: 28px; color: var(--text);
  }
</style>
</head>
<body>
<main class="sheet">

  <section class="card card--front" aria-label="Card front">
    <div class="pattern-band" role="img" aria-label="Scattered triangle pattern fading down from the top edge"></div>
    <div class="world-map" role="img" aria-label="Faint dotted world map"></div>
    <div class="brand">
      <span class="brand__mark"></span>
      <div class="brand__words">
        <span class="brand__name">BVS</span>
        <span class="brand__tagline">BRIGHTVALE SOLAR</span>
      </div>
    </div>
    <div class="web-link">
      <svg width="16" height="24" viewBox="0 0 16 24" aria-hidden="true">
        <rect x="1.5" y="1.5" width="13" height="21" rx="6.5" fill="none" stroke="#111" stroke-width="2"/>
        <line x1="8" y1="5" x2="8" y2="10" stroke="#111" stroke-width="2" stroke-linecap="round"/>
      </svg>
      <span>www.brightvalesolar.com</span>
    </div>
  </section>

  <section class="card card--back" aria-label="Card back">
    <div class="pattern-band" role="img" aria-label="Scattered yellow triangle pattern fading down from the top edge"></div>
    <div class="world-map" role="img" aria-label="Faint grey dotted world map"></div>
    <div class="brand">
      <span class="brand__mark"></span>
      <div class="brand__words">
        <span class="brand__name">BVS</span>
        <span class="brand__tagline">BRIGHTVALE SOLAR</span>
      </div>
    </div>
    <h1 class="form-title">Appointment</h1>
    <div class="form-panel">
      <p class="form-field" style="top:50px">Date:</p>
      <p class="form-field" style="top:140px">Time:</p>
      <p class="form-field" style="top:230px">Representative:</p>
      <p class="form-field" style="top:320px">Phone:</p>
    </div>
  </section>

</main>
</body>
</html>
```